HiItsJonBrell.com needs a modern, eye-catching business card design

My name is Jon Brell and I own a video training (software development industry) website. I need a business card design that is eye catching for when I travel to conferences or do seminars. I would prefer something simple but bold. Something along the lines of this: https://pixvaultstatic.example/gallery_img/530172/44018/44018_9917302_530172_image.jpg

Note that I do not have a specific logo, but I do have an caricature I use on my site of myself. I've not attached it because I'm not really a fan of having it on my business cards. I would prefer lettering instead of an image. You can go to my website (https://hiitsjonbrell.com) for inspiration.

I want to add the following information on my card (the order of these, their size, and their casing is up to you):

Jon Brell
jon@HiItsJonBrell.com
@HiItsJonBrell
HiItsJonBrell.com
vidsharehub.example/HiItsJonBrell

I would also like to have somewhere on the card a small ad that says "Get a free course at https://HiItsJonBrell.com/FreeCourse". Feel free to play with that wording or layout if you need. I would prefer this text to be at the bottom of the card and subtle. Some small eye-catching thing might be ok but nothing huge or garish.

I plan on printing this card at pressquill.example (https://www.pressquill.example/us/design-guidelines/business-cards.html). I would like it to be the standard size (3.66" x 2.16"). I would prefer rounded corners and horizontal orientation. This is a two-side design. I would prefer the side with all of the information be primarily white but I like color text (again, flexible on that). On the front side, I like simple. Maybe just HiItsJonBrell.com (casing on that is up to you - whatever looks and reads the best - that goes for all of the casing). As for font choices, I prefer a modern, clean font. For example, Open Sans Light can be a nice option.

Website Info (might be helpful for the card):
Color Palette

Darkest blue - #263246
Alternate blue - #2F4E6A
Light blue - #2A98C3
Orange - #FF6201
White - #FFFFFF

Font for Jon Brell Logo

Jellyka Estryas Handwriting
http://www.typecrate.example/jellyka_estryas_handwriting.font

Fonts for Site Content and VidShare Thumbnails

Lovelo (bold title font)
http://www.glyphmill.example/lovelo-font/

Open Sans (body font)
http://www.letterbarn.example/fonts/open-sans

Industry/Entity Type

Software Development

Contact Information for Business Card

Jon Brell
jon@HiItsJonBrell.com
@HiItsJonBrell
HiItsJonBrell.com
vidsharehub.example/HiItsJonBrell

Get a free course at https://HiItsJonBrell.com/FreeCourse

Colors

Designer to choose colors to be used in the design.

Requirements
Nice to have
• Modern color - maybe primarily a color on the front and then that color as an accent on the back.
Should not have
• Lots of colors - I LOVE color but do not want a rainbow of colors on the card.

```html
<!DOCTYPE html>
<html lang="en">
<head>
<meta charset="utf-8">
<title>HiItsJonBrell.com – Business Card</title>
<link rel="stylesheet" href="https://fonts.googleapis.com/css2?family=Open+Sans:wght@300;400;600&display=swap">
<style>
  :root {
    --stage: #232323;
    --card-dark: #050505;
    --code-green: #4cb84a;
    --card-green: #4db749;
    --ink: #141414;
    --card-w: 700px;
    --card-h: 413px;
    --radius: 26px;
  }
  * { box-sizing: border-box; margin: 0; padding: 0; }
  html, body {
    width: 1200px;
    height: 1000px;
    overflow: hidden;
    background: var(--stage);
    font-family: "Open Sans", Arial, sans-serif;
  }
  .canvas {
    position: relative;
    width: 1200px;
    height: 1000px;
  }
  .card {
    position: absolute;
    left: 250px;
    width: var(--card-w);
    height: var(--card-h);
    border-radius: var(--radius);
    overflow: hidden;
  }
  .card--front { top: 60px; background: var(--card-dark); }
  .card--back  { top: 527px; background: var(--card-green); color: var(--ink); }

  /* Front */
  .binary-field {
    position: absolute;
    inset: 0;
    background:
      repeating-linear-gradient(180deg, rgba(76,184,74,0.16) 0 18px, rgba(0,0,0,0) 18px 38px),
      radial-gradient(ellipse at center, #0d1a0c 0%, #050505 75%);
  }
  .front-domain {
    position: absolute;
    left: 0; right: 0;
    top: 50%;
    transform: translateY(-50%);
    text-align: center;
    font-weight: 600;
    font-size: 44px;
    letter-spacing: 0.3px;
    color: var(--code-green);
    background: var(--card-dark);
    padding: 4px 0;
    width: max-content;
    margin: 0 auto;
    padding: 2px 14px;
  }

  /* Back */
  .back-name {
    position: absolute;
    left: 0;
    width: 330px;
    top: 150px;
    text-align: center;
    font-weight: 300;
    font-size: 42px;
  }
  .back-divider {
    position: absolute;
    left: 338px;
    top: 60px;
    width: 2px;
    height: 240px;
    background: var(--ink);
  }
  .contact-list {
    position: absolute;
    left: 370px;
    top: 108px;
    list-style: none;
  }
  .contact-item {
    display: flex;
    align-items: center;
    gap: 12px;
    font-size: 18px;
    font-weight: 400;
    line-height: 36px;
  }
  .contact-icon { width: 18px; height: 18px; flex: none; }
  .promo {
    position: absolute;
    left: 0; right: 0;
    bottom: 26px;
    display: flex;
    justify-content: center;
    gap: 40px;
    font-size: 12px;
    font-weight: 400;
  }
</style>
</head>
<body>
<main class="canvas">

  <section class="card card--front" aria-label="Card front">
    <div class="binary-field" role="img" aria-label="Field of green binary digits covering the card"></div>
    <p class="front-domain">hiItsJonBrell.com</p>
  </section>

  <section class="card card--back" aria-label="Card back">
    <h1 class="back-name">Jon Brell</h1>
    <div class="back-divider"></div>
    <ul class="contact-list">
      <li class="contact-item">
        <svg class="contact-icon" viewBox="0 0 18 18" aria-hidden="true">
          <circle cx="9" cy="9" r="8" fill="var(--ink)"/>
          <ellipse cx="9" cy="9" rx="3.5" ry="7.5" fill="none" stroke="var(--card-green)" stroke-width="1.2"/>
          <line x1="1.5" y1="9" x2="16.5" y2="9" stroke="var(--card-green)" stroke-width="1.2"/>
        </svg>
        <span>HiItsJonBrell.com</span>
      </li>
      <li class="contact-item">
        <svg class="contact-icon" viewBox="0 0 18 18" aria-hidden="true">
          <rect x="1" y="3.5" width="16" height="11" fill="var(--ink)"/>
          <polyline points="1.5,4 9,10 16.5,4" fill="none" stroke="var(--card-green)" stroke-width="1.2"/>
        </svg>
        <span>jon@HiItsJonBrell.com</span>
      </li>
      <li class="contact-item">
        <svg class="contact-icon" viewBox="0 0 18 18" aria-hidden="true">
          <circle cx="9" cy="9" r="7" fill="var(--ink)"/>
        </svg>
        <span>@HiItsJonBrell</span>
      </li>
      <li class="contact-item">
        <svg class="contact-icon" viewBox="0 0 18 18" aria-hidden="true">
          <rect x="2" y="2" width="14" height="14" fill="var(--ink)"/>
        </svg>
        <span>vidsharehub.example/HiItsJonBrell</span>
      </li>
    </ul>
    <p class="promo">
      <span>A Complimentary Token :)</span>
      <span>https://HiItsJonBrell.com/FreeCourse</span>
    </p>
  </section>

</main>
</body>
</html>
```